Letterhead for paint manufacturing company

We need a letterhead for a paint manufacturing company called Corvane Industries Limited. We manufacture paint for construction companies as well as end consumers. We don't have a logo. Would like to see a design incorporating Pastel colours. We are based in Nigeria. Information to be included on the letterhead are:
Company name; Address: 12 plot D Amokwe Industrial Estate, Ilupeju, Ikeja; Phone numbers: 08061729350, 08072364918

Industry/Entity Type

Construction

```html
<!DOCTYPE html>
<html lang="en">
<head>
<meta charset="utf-8">
<title>Corvane Industries Limited – Letterhead Options</title>
<link rel="stylesheet" href="https://fonts.googleapis.com/css2?family=Archivo:wght@700&family=Marcellus+SC&family=PT+Sans:wght@700&display=swap">
<style>
  :root {
    --backdrop: #e9e6e2;
    --paper: #ffffff;
    --ink: #111111;
    --footer-ink: #3a3a3a;
    --stripe-pink: #e9a3ab;
    --stripe-lavender: #c8a2cf;
    --stripe-salmon: #f2b59e;
    --stripe-peach: #f7c99a;
    --stripe-apricot: #f6d28f;
    --stripe-yellow: #f3ea9c;
    --stripe-green: #b7dba2;
    --stripe-blue: #95afdc;
    --mauve: #c792bf;
    --on-mauve: #ffffff;
  }
  * { margin: 0; padding: 0; box-sizing: border-box; }
  html, body { width: 1200px; height: 649px; overflow: hidden; }
  body { background: var(--backdrop); position: relative; }

  .sheet {
    position: absolute;
    top: 53px;
    width: 383px;
    height: 542px;
    background: var(--paper);
    box-shadow: 0 4px 14px rgba(0,0,0,0.18);
    overflow: hidden;
  }
  .sheet--stripes { left: 155px; }
  .sheet--mauve { left: 646px; }

  /* Option one: pastel stripes */
  .stripe-band { position: absolute; left: 0; width: 100%; display: flex; flex-direction: column; }
  .stripe-band--top { top: 0; height: 51px; }
  .stripe-band--bottom { bottom: 0; height: 22px; }
  .stripe { flex: 1 1 0; }
  .stripe--pink { background: var(--stripe-pink); }
  .stripe--lavender { background: var(--stripe-lavender); }
  .stripe--salmon { background: var(--stripe-salmon); }
  .stripe--peach { background: var(--stripe-peach); }
  .stripe--apricot { background: var(--stripe-apricot); }
  .stripe--yellow { background: var(--stripe-yellow); }
  .stripe--green { background: var(--stripe-green); }
  .stripe--blue { background: var(--stripe-blue); }

  .stripes-title {
    position: absolute; top: 14px; left: 0; width: 100%;
    text-align: center;
    font-family: "Archivo", Arial, sans-serif; font-weight: 700;
    font-size: 15px; letter-spacing: 0.4px; color: var(--ink);
  }
  .stripes-contact {
    position: absolute; bottom: 6px; left: 0; width: 100%;
    text-align: center;
    font-family: "PT Sans", Arial, sans-serif; font-weight: 700;
    font-size: 5.6px; color: var(--footer-ink); white-space: nowrap;
  }

  /* Option two: mauve bands */
  .mauve-header {
    position: absolute; top: 0; left: 0; width: 100%; height: 70px;
    background: var(--mauve);
    display: flex; align-items: center; justify-content: center;
  }
  .mauve-title {
    font-family: "Marcellus SC", Georgia, serif;
    font-size: 19px; letter-spacing: 0.8px; color: var(--on-mauve);
  }
  .mauve-footer {
    position: absolute; bottom: 0; left: 0; width: 100%; height: 32px;
    background: var(--mauve);
    border-top: 1.5px solid var(--mauve);
  }
  .mauve-footer::before {
    content: ""; position: absolute; top: 3px; left: 0; width: 100%; height: 1.5px;
    background: var(--on-mauve);
  }
  .mauve-contact {
    position: absolute; top: 8px; left: 0; width: 100%;
    text-align: center;
    font-family: "PT Sans", Arial, sans-serif; font-weight: 700;
    font-size: 6.4px; line-height: 11px; color: var(--on-mauve);
  }
</style>
</head>
<body>
  <section class="sheet sheet--stripes" aria-label="Letterhead option with pastel stripes">
    <div class="stripe-band stripe-band--top">
      <span class="stripe stripe--pink"></span>
      <span class="stripe stripe--lavender"></span>
      <span class="stripe stripe--salmon"></span>
      <span class="stripe stripe--peach" style="flex-grow:1.6"></span>
      <span class="stripe stripe--apricot" style="flex-grow:1.4"></span>
      <span class="stripe stripe--yellow"></span>
      <span class="stripe stripe--green"></span>
      <span class="stripe stripe--blue"></span>
    </div>
    <h1 class="stripes-title">Corvane Industries Limited</h1>

    <div class="stripe-band stripe-band--bottom">
      <span class="stripe stripe--pink"></span>
      <span class="stripe stripe--lavender"></span>
      <span class="stripe stripe--peach" style="flex-grow:2"></span>
      <span class="stripe stripe--yellow"></span>
      <span class="stripe stripe--green"></span>
      <span class="stripe stripe--blue"></span>
    </div>
    <p class="stripes-contact">12 plot D Amokwe Industrial Estate, Ilupeju, Ikeja &nbsp; PH: 08061729350, 08072364918</p>
  </section>

  <section class="sheet sheet--mauve" aria-label="Letterhead option with mauve bands">
    <header class="mauve-header">
      <h1 class="mauve-title">Corvane Industries Limited</h1>
    </header>
    <footer class="mauve-footer">
      <p class="mauve-contact">12 plot D Amokwe Industrial Estate, Ilupeju, Ikeja<br>08061729350, 08072364918</p>
    </footer>
  </section>
</body>
</html>
```